The Cactus Lantern Food Truck, Specializes in Tacos, Quesadillas, Burritos The Cactus Lantern Dog and The Cactus Lantern Bowl, which is all the ingredients of a burrito mixed in a bowl. Meat options include Steak, Chicken, Shrimp and Pork. Attached fins a Picture of our food truck. we want to keep that color scheme

Colors
9bcb3c
ec1f27

Requirements
Must have
• Pictures of all the items we offer, main colors for the design should be lime bright green and red. font should be easily readable.
Nice to have
• picture of a lime green food truck

```html
<!DOCTYPE html>
<html lang="en">
<head>
<meta charset="utf-8">
<title>Cactus Lantern Food Truck Menu</title>
<link rel="stylesheet" href="https://fonts.googleapis.com/css2?family=Alfa+Slab+One&family=Montserrat:wght@800&display=swap">
<style>
  :root {
    --page: #e9e6e1;
    --board: #2a2a2b;
    --board-edge: #1f1f20;
    --lime: #9bcb3c;
    --red: #ec1f27;
    --chalk-red: #c8424a;
    --chalk-white: #f4f2ee;
    --doodle: #4a4a4b;
  }
  html, body {
    margin: 0;
    width: 1200px;
    height: 1200px;
    overflow: hidden;
    background: var(--page);
  }
  .canvas {
    position: relative;
    width: 1200px;
    height: 1200px;
  }
  .menu-board {
    position: absolute;
    left: 230px;
    top: 40px;
    width: 740px;
    height: 1120px;
    background: radial-gradient(ellipse at 50% 40%, #333334 0%, var(--board) 55%, var(--board-edge) 100%);
    overflow: hidden;
  }
  .doodle {
    position: absolute;
    width: 46px;
    height: 46px;
    border-radius: 50%;
    background: var(--doodle);
    opacity: 0.55;
  }
  .menu-title {
    position: absolute;
    top: 120px;
    left: 0;
    width: 100%;
    display: flex;
    justify-content: center;
    align-items: center;
    gap: 14px;
  }
  .menu-title h1 {
    margin: 0;
    font-family: "Alfa Slab One", serif;
    font-weight: 400;
    font-size: 76px;
    letter-spacing: 2px;
    color: var(--lime);
  }
  .price-frame {
    position: absolute;
    left: 80px;
    top: 300px;
    width: 580px;
    height: 640px;
    border: 3px dashed var(--lime);
    border-radius: 14px;
    box-sizing: border-box;
    padding: 44px 34px 0 30px;
  }
  .price-list {
    list-style: none;
    margin: 0;
    padding: 0;
  }
  .price-row {
    display: flex;
    align-items: center;
    height: 62px;
    font-family: "Montserrat", sans-serif;
    font-weight: 800;
    color: var(--chalk-white);
  }
  .item-mark {
    width: 12px;
    height: 3px;
    background: var(--chalk-white);
    margin-right: 12px;
    flex: none;
  }
  .item-name {
    font-size: 27px;
    letter-spacing: 0.5px;
    white-space: nowrap;
  }
  .item-leader {
    flex: 1;
    height: 4px;
    margin: 0 16px;
    background: var(--chalk-red);
    border-radius: 2px;
    transform: rotate(-3deg);
  }
  .item-price {
    display: flex;
    align-items: flex-start;
    gap: 16px;
    flex: none;
  }
  .price-currency { font-size: 32px; }
  .price-cents { font-size: 19px; margin-top: -8px; }
</style>
</head>
<body>
<div class="canvas">
  <section class="menu-board">
    <div class="doodle" role="img" aria-label="Chalk doodle of a vegetable" style="left:30px;top:40px"></div>
    <div class="doodle" role="img" aria-label="Chalk doodle of leaves" style="left:240px;top:30px"></div>
    <div class="doodle" role="img" aria-label="Chalk doodle of a pepper" style="left:430px;top:20px"></div>
    <div class="doodle" role="img" aria-label="Chalk doodle of a drink cup" style="left:650px;top:80px"></div>
    <div class="doodle" role="img" aria-label="Chalk doodle of a burger" style="left:14px;top:380px"></div>
    <div class="doodle" role="img" aria-label="Chalk doodle of fries" style="left:10px;top:640px"></div>
    <div class="doodle" role="img" aria-label="Chalk doodle of a vegetable" style="left:680px;top:450px"></div>
    <div class="doodle" role="img" aria-label="Chalk doodle of a tomato" style="left:680px;top:640px"></div>
    <div class="doodle" role="img" aria-label="Chalk doodle of a mushroom" style="left:60px;top:980px"></div>
    <div class="doodle" role="img" aria-label="Chalk doodle of a pepper" style="left:300px;top:1040px"></div>
    <div class="doodle" role="img" aria-label="Chalk doodle of a drink cup" style="left:520px;top:1000px"></div>
    <div class="doodle" role="img" aria-label="Chalk doodle of a lemon" style="left:660px;top:940px"></div>

    <header class="menu-title">
      <svg width="30" height="60" viewBox="0 0 30 60" aria-hidden="true">
        <g stroke="#9bcb3c" stroke-width="4" stroke-linecap="round">
          <line x1="4" y1="10" x2="22" y2="20"/>
          <line x1="2" y1="30" x2="24" y2="30"/>
          <line x1="4" y1="50" x2="22" y2="40"/>
        </g>
      </svg>
      <h1>MENU</h1>
      <svg width="30" height="60" viewBox="0 0 30 60" aria-hidden="true">
        <g stroke="#9bcb3c" stroke-width="4" stroke-linecap="round">
          <line x1="26" y1="10" x2="8" y2="20"/>
          <line x1="28" y1="30" x2="6" y2="30"/>
          <line x1="26" y1="50" x2="8" y2="40"/>
        </g>
      </svg>
    </header>

    <div class="price-frame">
      <ul class="price-list">
        <li class="price-row"><span class="item-mark"></span><span class="item-name">TACOS</span><span class="item-leader"></span><span class="item-price"><span class="price-currency">$</span><span class="price-cents">.00</span></span></li>
        <li class="price-row"><span class="item-mark"></span><span class="item-name">QUESADILLAS</span><span class="item-leader"></span><span class="item-price"><span class="price-currency">$</span><span class="price-cents">.00</span></span></li>
        <li class="price-row"><span class="item-mark"></span><span class="item-name">BURRITOS</span><span class="item-leader"></span><span class="item-price"><span class="price-currency">$</span><span class="price-cents">.00</span></span></li>
        <li class="price-row"><span class="item-mark"></span><span class="item-name">CACTUS LANTERN BOWL</span><span class="item-leader"></span><span class="item-price"><span class="price-currency">$</span><span class="price-cents">.00</span></span></li>
        <li class="price-row"><span class="item-mark"></span><span class="item-name">CACTUS LANTERN DOG</span><span class="item-leader"></span><span class="item-price"><span class="price-currency">$</span><span class="price-cents">.00</span></span></li>
        <li class="price-row"><span class="item-mark"></span><span class="item-name">MEATS - STEAK</span><span class="item-leader"></span><span class="item-price"><span class="price-currency">$</span><span class="price-cents">.00</span></span></li>
        <li class="price-row"><span class="item-mark"></span><span class="item-name">CHICKEN</span><span class="item-leader"></span><span class="item-price"><span class="price-currency">$</span><span class="price-cents">.00</span></span></li>
        <li class="price-row"><span class="item-mark"></span><span class="item-name">PORK</span><span class="item-leader"></span><span class="item-price"><span class="price-currency">$</span><span class="price-cents">.00</span></span></li>
        <li class="price-row"><span class="item-mark"></span><span class="item-name">SHRIMP</span><span class="item-leader"></span><span class="item-price" style="visibility:hidden"><span class="price-currency">$</span><span class="price-cents">.00</span></span></li>
      </ul>
    </div>
  </section>
</div>
</body>
</html>
```